Christmas Card 2017

We are looking for a Christmas Card that uses our team photo and our logo. We would also like our demographic information used as follows:
782 Larkmoor Ste. B
Webster, TX 77412
Phone: 832-417-2263 Fax 832-417-2264
www.pinecrestcardio.example

We are a cardiology group practice. If you could use red and black colors with maybe some silver or gold, whichever looks better.

We would like the design to be a foldable type Christmas Card.

```html
<!DOCTYPE html>
<html lang="en">
<head>
<meta charset="utf-8">
<title>Pinecrest Cardio Christmas Card</title>
<link href="https://fonts.googleapis.com/css2?family=Open+Sans:wght@400;700&family=Yellowtail&display=swap" rel="stylesheet">
<style>
  :root {
    --backdrop: #dcddd6;
    --paper: #f6f6ef;
    --red: #c8102e;
    --red-deep: #8e0a17;
    --red-bright: #d8232f;
    --ink: #1c1c1c;
    --fold: #d9d9d0;
    --photo-warm: #8a6f5c;
    --photo-dark: #3a2a24;
    --photo-light: #c9b9a6;
  }
  * { box-sizing: border-box; margin: 0; padding: 0; }
  html, body { width: 1200px; height: 800px; overflow: hidden; }
  body {
    background: var(--backdrop);
    font-family: "Open Sans", Arial, sans-serif;
    color: var(--ink);
    position: relative;
  }

  /* Inside spread */
  .card-inside {
    position: absolute;
    left: 50px;
    top: 220px;
    width: 700px;
    height: 360px;
    background: var(--paper);
    box-shadow: 0 6px 18px rgba(0,0,0,.18);
    display: flex;
    flex-direction: column;
  }
  .team-photo {
    height: 258px;
    background: linear-gradient(180deg, var(--photo-dark) 0%, var(--photo-warm) 45%, var(--photo-light) 100%);
  }
  .inside-band {
    flex: 1;
    display: flex;
    border-top: 4px solid var(--red);
    border-bottom: 12px solid var(--red);
    position: relative;
  }
  .inside-band::after {
    content: "";
    position: absolute;
    left: 350px;
    top: -262px;
    bottom: -12px;
    width: 1px;
    background: var(--fold);
  }
  .inside-left, .inside-right {
    width: 350px;
    display: flex;
    align-items: center;
    padding: 0 34px;
  }
  .contact-block {
    font-size: 12px;
    line-height: 1.5;
    color: var(--ink);
  }

  /* Logo placement */
  .practice-name {
    display: flex;
    align-items: center;
    gap: 9px;
    font-family: "Open Sans", Arial, sans-serif;
    font-weight: 700;
    font-size: 20px;
    color: var(--red);
    letter-spacing: .5px;
  }
  .practice-name .mark {
    width: 12px;
    height: 12px;
    background: var(--red);
  }

  /* Front cover */
  .card-front {
    position: absolute;
    left: 800px;
    top: 220px;
    width: 350px;
    height: 360px;
    background: var(--paper);
    box-shadow: 0 6px 18px rgba(0,0,0,.18);
    display: flex;
    flex-direction: column;
  }
  .front-field {
    height: 262px;
    position: relative;
    background:
      linear-gradient(180deg, rgba(255,255,255,.55) 0%, rgba(255,255,255,0) 14%, rgba(255,255,255,0) 74%, rgba(255,255,255,.6) 100%),
      radial-gradient(ellipse at 55% 45%, var(--red-bright) 0%, var(--red) 50%, var(--red-deep) 100%);
    display: flex;
    flex-direction: column;
    align-items: center;
    justify-content: center;
    color: #fff;
  }
  .greeting-main {
    font-family: "Yellowtail", cursive;
    font-size: 34px;
    line-height: 1;
  }
  .greeting-sub {
    font-size: 12px;
    margin-top: 2px;
    margin-left: 40px;
  }
  .front-footer {
    flex: 1;
    display: flex;
    align-items: center;
    justify-content: center;
  }
</style>
</head>
<body>

  <section class="card-inside">
    <div class="team-photo" role="img" aria-label="Team photo of the cardiology staff in white coats and black scrubs, seated and standing in the clinic lobby"></div>
    <div class="inside-band">
      <div class="inside-left">
        <div class="practice-name"><span class="mark"></span>Pinecrest Cardio</div>
      </div>
      <div class="inside-right">
        <address class="contact-block" style="font-style: normal;">
          782 Larkmoor Ste. B<br>
          Webster, TX 77412<br>
          Phone: 832-417-2263 Fax 832-417-2264<br>
          www.pinecrestcardio.example
        </address>
      </div>
    </div>
  </section>

  <section class="card-front">
    <div class="front-field" role="img" aria-label="Red field framed by white snowflake borders at top and bottom">
      <p class="greeting-main">Merry Christmas</p>
      <p class="greeting-sub">&amp; Happy New Year</p>
    </div>
    <div class="front-footer">
      <div class="practice-name"><span class="mark"></span>Pinecrest Cardio</div>
    </div>
  </section>

</body>
</html>
```